Marlow Ridge Dental business card

Business card would have following info:

Alden R. Kasprzak, DMD, FAGD
General Dentist
email: office@marlowridgedental.example
phone: 617-490-3867
fax: 617-490-3867
website: marlowridgedental.example

second side would have lines for:

appointment date
appointment time

```html
<!DOCTYPE html>
<html lang="en">
<head>
<meta charset="utf-8">
<title>Marlow Ridge Dental business card</title>
<link href="https://fonts.googleapis.com/css2?family=Arimo:wght@400;700&display=swap" rel="stylesheet">
<style>
  :root {
    --backdrop: #979797;
    --card: #ffffff;
    --ink: #2b2b2b;
    --ink-soft: #3a3a3a;
    --rule: #333333;
  }
  * { margin: 0; padding: 0; box-sizing: border-box; }
  html, body {
    width: 1200px; height: 1059px; overflow: hidden;
    background: var(--backdrop);
    font-family: "Arimo", Arial, sans-serif;
    color: var(--ink);
  }
  .canvas { position: relative; width: 1200px; height: 1059px; }
  .card {
    position: absolute;
    background: var(--card);
    border-radius: 24px;
  }
  .card-front { left: 256px; top: 89px; width: 688px; height: 390px; }
  .card-back { left: 253px; top: 569px; width: 694px; height: 394px; }

  .doctor-name {
    position: absolute; left: 0; right: 0; top: 105px;
    text-align: center;
    font-weight: 700; font-size: 28px; letter-spacing: 0.2px;
    color: var(--ink);
  }
  .doctor-role {
    position: absolute; left: 0; right: 0; top: 146px;
    text-align: center;
    font-size: 22px; color: var(--ink-soft);
  }
  .contact-divider {
    position: absolute; left: 333px; top: 281px;
    width: 1.5px; height: 39px; background: var(--rule);
  }
  .contact-column {
    position: absolute; top: 276px;
    font-size: 18.5px; line-height: 25px; color: var(--ink-soft);
  }
  .contact-column.left { right: 366px; text-align: right; }
  .contact-column.right { left: 349px; }
  .contact-line { display: flex; align-items: center; gap: 6px; white-space: nowrap; }
  .contact-column.left .contact-line { justify-content: flex-end; }
  .contact-line svg { width: 13px; height: 13px; fill: var(--ink); flex: none; }

  .field-label {
    position: absolute; left: 46px;
    font-size: 18.5px; color: var(--ink-soft);
  }
  .field-rule {
    position: absolute; left: 45px; width: 604px;
    height: 1.5px; background: var(--rule);
  }
  .date-label { top: 126px; }
  .date-rule { top: 171px; }
  .time-label { top: 223px; }
  .time-rule { top: 267px; }
</style>
</head>
<body>
<div class="canvas">
  <section class="card card-front">
    <h1 class="doctor-name">ALDEN R. KASPRZAK, DMD, FAGD</h1>
    <p class="doctor-role">General Dentist</p>

    <div class="contact-column left">
      <div class="contact-line">617-490-3867
        <svg viewBox="0 0 16 16" aria-label="fax"><rect x="4" y="1" width="8" height="4"/><rect x="1" y="6" width="14" height="6" rx="1"/><rect x="4" y="10" width="8" height="5" fill="#fff" stroke="#2b2b2b" stroke-width="1.5"/></svg>
      </div>
      <div class="contact-line">www.marlowridgedental.example
        <svg viewBox="0 0 16 16" aria-label="website"><circle cx="8" cy="8" r="7"/><path d="M5 4c2 1 1 3 3 3s1 3-1 4M10 3c0 2 2 2 3 3" stroke="#fff" stroke-width="1.3" fill="none"/></svg>
      </div>
    </div>

    <div class="contact-divider"></div>

    <div class="contact-column right">
      <div class="contact-line">
        <svg viewBox="0 0 16 16" aria-label="phone"><path d="M1 6c0-2 3-3 7-3s7 1 7 3v1h-3V5.5H4V7H1z"/><path d="M4 8h8l2 6H2z"/><circle cx="8" cy="11" r="1.6" fill="#fff"/></svg>
        617-490-3867
      </div>
      <div class="contact-line">
        <svg viewBox="0 0 16 16" aria-label="email"><path d="M1 7l7-5 7 5v8H1z"/><path d="M1 7l7 5 7-5" stroke="#fff" stroke-width="1.2" fill="none"/><rect x="4.5" y="4.5" width="7" height="4" fill="#fff"/></svg>
        office@marlowridgedental.example
      </div>
    </div>
  </section>

  <section class="card card-back">
    <p class="field-label date-label">Appointment Date :</p>
    <div class="field-rule date-rule"></div>
    <p class="field-label time-label">Appointment Time :</p>
    <div class="field-rule time-rule"></div>
  </section>
</div>
</body>
</html>
```